hair salon business Card Design

My business name is Hair & Beauty @ Corvale I want a Hot Pink and black business card with a loyalty program on the back after every 2nd haircut the third has $5 off and I will whole punch the squares My business phone number is (07) 58 913 640 address is Shop 4 3/9 Brambury st Corvale Qld 4570 find us on facebook should be on the card somewhere with the facebook logo also a space alocated for your next appointment date n time also would like your har stylists name is Tez on the card somewhere easy to read you can check out my facebook site for images of my logo n shop signage

Industry/Entity Type

Hair

```html
<!DOCTYPE html>
<html lang="en">
<head>
<meta charset="utf-8">
<title>Hair &amp; Beauty @ Corvale – Business Card</title>
<link rel="stylesheet" href="https://fonts.googleapis.com/css2?family=Delius&family=PT+Sans+Narrow&family=Open+Sans&family=Courgette&display=swap">
<style>
  :root {
    --hot-pink: #e3127f;
    --card-dark: #1c1c1e;
    --card-mid: #2e2e31;
    --text-light: #f2f2f2;
    --backdrop: #e9e6e3;
  }
  * { box-sizing: border-box; margin: 0; padding: 0; }
  html, body { width: 1200px; height: 1200px; overflow: hidden; }
  body {
    background: var(--backdrop);
    display: flex; align-items: center; justify-content: center;
  }
  .business-card {
    position: relative;
    width: 1000px; height: 572px;
    background: linear-gradient(160deg, var(--card-mid) 0%, var(--card-dark) 70%);
    box-shadow: 0 10px 30px rgba(0,0,0,.25);
    color: var(--text-light);
    overflow: hidden;
  }
  .brand-header {
    position: absolute; left: 48px; top: 52px;
    display: flex; align-items: center; gap: 26px;
  }
  .brand-mark {
    width: 46px; height: 46px; background: var(--hot-pink);
  }
  .brand-name {
    font-family: "Delius", sans-serif;
    font-size: 54px; color: var(--hot-pink); letter-spacing: .5px;
  }
  .header-rule {
    position: absolute; left: 0; right: 0; top: 152px;
    height: 8px;
    border-top: 2px solid var(--hot-pink);
    border-bottom: 2px solid var(--hot-pink);
  }
  .contact-item {
    position: absolute;
    display: flex; align-items: center; gap: 16px;
    font-family: "PT Sans Narrow", sans-serif;
    font-size: 31px; color: var(--text-light);
  }
  .contact-item svg { width: 30px; height: 34px; fill: var(--hot-pink); flex: none; }
  .contact-address { left: 52px; top: 196px; }
  .contact-phone { left: 52px; top: 276px; }
  .contact-social { left: 480px; top: 166px; }
  .social-dot { width: 26px; height: 26px; border-radius: 50%; background: var(--hot-pink); flex: none; }
  .appointment-box {
    position: absolute; left: 560px; top: 250px;
    width: 400px; height: 170px;
    border: 3px solid var(--hot-pink);
    padding: 24px 22px;
    font-family: "Open Sans", sans-serif;
    font-size: 22px; color: var(--text-light);
  }
  .loyalty-ribbon {
    position: absolute; left: 40px; top: 392px;
    width: 470px; height: 140px;
    transform: rotate(-9deg);
  }
  .loyalty-ribbon svg { position: absolute; inset: 0; width: 100%; height: 100%; }
  .loyalty-text {
    position: absolute; left: 70px; right: 60px; top: 34px;
    font-family: "Courgette", cursive;
    font-size: 27px; line-height: 1.2; color: #fff;
  }
</style>
</head>
<body>
  <main class="business-card">
    <header class="brand-header">
      <span class="brand-mark"></span>
      <h1 class="brand-name">Hair &amp; Beauty @ Corvale</h1>
    </header>
    <div class="header-rule"></div>

    <div class="contact-item contact-social">
      <span class="social-dot"></span>
      <span>Hair-Beauty-at-Corvale</span>
    </div>

    <div class="contact-item contact-address">
      <svg viewBox="0 0 24 28" aria-hidden="true"><path d="M12 0C5.4 0 0 5.2 0 11.6 0 19.5 12 28 12 28s12-8.5 12-16.4C24 5.2 18.6 0 12 0zm0 16a4.5 4.5 0 1 1 0-9 4.5 4.5 0 0 1 0 9z"/></svg>
      <span>Shop 4 3/9 Brambury st Corvale Qld 4570</span>
    </div>

    <div class="contact-item contact-phone">
      <svg viewBox="0 0 24 28" aria-hidden="true"><path d="M6.5 1 9.8 7.2c.4.8.2 1.7-.5 2.2L7.3 11c1.2 3.2 3.3 6 6 8l2-1.6c.7-.5 1.6-.5 2.2.1l5 4.8c.6.6.6 1.6 0 2.2l-2 2c-1.3 1.2-3.2 1.5-4.8.8C8.4 24.2 2.6 16.6 1.2 8c-.3-1.7.4-3.4 1.7-4.4L4.4 2.4c.7-.6 1.7-.4 2.1.4z"/></svg>
      <span>(07) 58 913 640</span>
    </div>

    <section class="appointment-box">Next appointment Date &amp; Time</section>

    <div class="loyalty-ribbon">
      <svg viewBox="0 0 470 140" preserveAspectRatio="none" aria-hidden="true">
        <polygon points="0,18 60,18 60,0 470,0 440,60 470,122 410,122 410,140 0,140 30,80" fill="#e3127f"/>
        <polygon points="60,18 60,30 30,18" fill="#9c0a56"/>
        <polygon points="410,122 410,110 440,122" fill="#9c0a56"/>
      </svg>
      <p class="loyalty-text">After every 2nd haircut<br>the third has $5 off</p>
    </div>
  </main>
</body>
</html>
```